Webbanner-Design für Führungskräfte-Coach
Danke für Ihr Engagement und die einwandfreie Abwicklung.
Zielgruppe
Ich coache Führungskräfte und Teams im Verkauf. Haupt-Keywort und Haupt-Thema:
Führung im Vertrieb. Das Design soll Führungskräften mit Verkaufsfunktionen gefallen.
Aufgabenstellung
Gemäss Memo (Datei: RBF-Banner-Memo).

```html
<!DOCTYPE html>
<html lang="de">
<head>
<meta charset="utf-8">
<title>Webbanner – Führung im Vertrieb</title>
<link rel="stylesheet" href="https://fonts.googleapis.com/css2?family=Arimo:wght@400;700&display=swap">
<style>
  :root {
    --page-bg: #ffffff;
    --panel-dark: #2f2f31;
    --stripe-blue: #3569c9;
    --sky-top: #5b8ed8;
    --sky-bottom: #a9c8f1;
    --headline-blue: #2d62c3;
    --cta-red: #a20f10;
    --text-light: #ffffff;
    --cloud: #f3f7fd;
    --portrait-dark: #2a2c33;
    --portrait-light: #8fa6c6;
  }
  html, body {
    margin: 0;
    width: 1200px;
    height: 1200px;
    overflow: hidden;
    background: var(--page-bg);
  }
  .stage {
    width: 1200px;
    height: 1200px;
    display: flex;
    align-items: center;
    justify-content: center;
  }
  .banner {
    width: 1100px;
    height: 416px;
    display: block;
    font-family: "Arimo", Arial, sans-serif;
  }
  .brand-name { font-weight: 700; font-size: 9px; fill: var(--text-light); }
  .brand-sub { font-weight: 400; font-size: 6.4px; fill: var(--text-light); }
  .web-link { font-size: 11px; fill: var(--text-light); }
  .headline { font-size: 17px; fill: var(--headline-blue); }
  .cta-text { font-weight: 700; font-size: 15.5px; fill: var(--text-light); }
</style>
</head>
<body>
<main class="stage">
  <svg class="banner" viewBox="0 0 505 191" xmlns="http://www.w3.org/2000/svg">
    <defs>
      <linearGradient id="sky" x1="0" y1="0" x2="0" y2="1">
        <stop offset="0" stop-color="var(--sky-top)"/>
        <stop offset="1" stop-color="var(--sky-bottom)"/>
      </linearGradient>
      <radialGradient id="cloudGlow" cx="0.5" cy="0.5" r="0.5">
        <stop offset="0" stop-color="var(--cloud)" stop-opacity="0.95"/>
        <stop offset="1" stop-color="var(--cloud)" stop-opacity="0"/>
      </radialGradient>
      <linearGradient id="portrait" x1="0" y1="0" x2="0" y2="1">
        <stop offset="0" stop-color="var(--portrait-light)"/>
        <stop offset="0.45" stop-color="var(--portrait-dark)"/>
        <stop offset="1" stop-color="var(--portrait-dark)"/>
      </linearGradient>
    </defs>

    <rect class="sky" x="0" y="0" width="505" height="191" fill="url(#sky)"/>

    <ellipse class="cloud-arrow" cx="262" cy="60" rx="75" ry="38" fill="url(#cloudGlow)"
             role="img" aria-label="Foto: Wolke in Form eines nach oben weisenden Pfeils"/>

    <polygon class="accent-stripe" points="0,124 455,0 468,0 0,136" fill="var(--stripe-blue)"/>
    <polygon class="brand-panel" points="0,0 455,0 0,124" fill="var(--panel-dark)"/>

    <g class="brand">
      <rect x="11" y="12" width="20" height="20" fill="var(--text-light)"/>
      <text class="brand-name" x="40" y="22">Rehberg</text>
      <text class="brand-sub" x="40" y="30">Coaching &amp; Training GmbH</text>
    </g>

    <text class="web-link" x="18" y="54" text-decoration="underline">www.rbf.ch</text>

    <rect class="portrait" x="360" y="10" width="145" height="181" fill="url(#portrait)"
          role="img" aria-label="Porträtfoto des Coaches im dunklen Sakko und hellblauen Hemd"/>

    <text class="headline" x="64" y="133">Sie suchen einen Coach für</text>

    <rect class="cta-box" x="12" y="147" width="331" height="27" fill="var(--cta-red)"/>
    <text class="cta-text" x="20" y="166">Führungskräfte und Teams im Vertrieb?</text>
  </svg>
</main>
</body>
</html>
```